K.T.L Electrical Services Pty Ltd

Electrical contracting business. I have a base for the design which i like. The contact number needs to be changed to 0491736250 and the O made more solid and level with the rest of the letters. If you have any other ideas of what would make it better I'm happy to see them.

The back side to be written as dot points with the following:
- Residential & Commercial
- Maintenance
- PV & Battery servicing
- EV Chargers

```html
<!DOCTYPE html>
<html lang="en">
<head>
<meta charset="utf-8">
<title>K.T.L Electrical Services – Business Card</title>
<link rel="stylesheet" href="https://fonts.googleapis.com/css2?family=Poppins:wght@300;400;500;600&display=swap">
<style>
  :root {
    --page: #1d1c21;
    --card: #23282a;
    --teal: #93b3b3;
    --tan: #d4a272;
    --ink: #e6eae9;
    --muted: #c9d2d1;
  }
  * { box-sizing: border-box; margin: 0; padding: 0; }
  html, body { width: 1200px; height: 801px; overflow: hidden; background: var(--page); }
  body { font-family: "Poppins", sans-serif; position: relative; }

  .card {
    position: absolute;
    width: 540px;
    height: 310px;
    background: var(--card);
    border-radius: 4px;
    overflow: hidden;
    box-shadow: 0 18px 40px rgba(0,0,0,.45);
  }
  .card--front { left: 40px; top: 245px; }
  .card--back  { left: 620px; top: 245px; }

  /* Front */
  .brand { position: absolute; left: 34px; top: 34px; display: flex; align-items: center; gap: 14px; }
  .brand__dot { width: 54px; height: 54px; border-radius: 50%; background: var(--teal); }
  .brand__text { display: flex; flex-direction: column; }
  .brand__name { font-weight: 300; font-size: 50px; line-height: 1; letter-spacing: 4px; color: var(--teal); }
  .brand__full { font-weight: 500; font-size: 11px; letter-spacing: 2.4px; color: var(--teal); margin-top: 6px; }
  .brand__licence { font-weight: 400; font-size: 11px; letter-spacing: 1px; color: var(--tan); margin-top: 2px; }

  .person { position: absolute; left: 34px; top: 160px; }
  .person__name { font-weight: 600; font-size: 22px; color: var(--teal); line-height: 1.1; }
  .person__role { font-weight: 400; font-size: 13px; color: var(--ink); margin-top: 2px; }
  .person__rule { width: 56px; height: 2px; background: var(--tan); margin-top: 8px; }

  .contact { position: absolute; left: 34px; top: 238px; list-style: none; }
  .contact__item { display: flex; align-items: center; gap: 10px; font-size: 13px; color: var(--ink); line-height: 1.7; }
  .contact__icon { width: 13px; height: 13px; fill: var(--teal); }

  /* Back */
  .services { position: absolute; left: 40px; top: 44px; }
  .services__title { font-weight: 500; font-size: 20px; letter-spacing: .5px; color: var(--teal); }
  .services__rule { width: 62px; height: 2px; background: var(--tan); margin-top: 6px; }
  .services__list { list-style: none; margin-top: 18px; }
  .services__item { display: flex; align-items: center; gap: 12px; font-size: 15px; color: var(--ink); line-height: 2; }
  .services__bolt { width: 11px; height: 15px; fill: var(--tan); }

  .accent { position: absolute; inset: 0; width: 540px; height: 310px; }
</style>
</head>
<body>

  <section class="card card--front" aria-label="Business card front">
    <div class="brand">
      <span class="brand__dot"></span>
      <div class="brand__text">
        <span class="brand__name">K.T.L</span>
        <span class="brand__full">ELECTRICAL SERVICES PTY LTD</span>
        <span class="brand__licence">EC 20418</span>
      </div>
    </div>

    <div class="person">
      <p class="person__name">Dana Whitfield</p>
      <p class="person__role">Director</p>
      <div class="person__rule"></div>
    </div>

    <ul class="contact">
      <li class="contact__item">
        <svg class="contact__icon" viewBox="0 0 24 24"><path d="M6.6 10.8a15.1 15.1 0 0 0 6.6 6.6l2.2-2.2c.3-.3.7-.4 1-.2 1.1.4 2.3.6 3.6.6.6 0 1 .4 1 1V20c0 .6-.4 1-1 1A17 17 0 0 1 3 4c0-.6.4-1 1-1h3.5c.6 0 1 .4 1 1 0 1.3.2 2.5.6 3.6.1.3 0 .7-.2 1z"/></svg>
        0491 736 250
      </li>
      <li class="contact__item">
        <svg class="contact__icon" viewBox="0 0 24 24"><path d="M2 5h20v14H2z M2 5l10 8 10-8" fill="var(--teal)"/><path d="M3 6l9 7 9-7" fill="none" stroke="var(--card)" stroke-width="1.6"/></svg>
        admin@ktl-elect.com
      </li>
    </ul>
  </section>

  <section class="card card--back" aria-label="Business card back">
    <svg class="accent" viewBox="0 0 540 310" aria-hidden="true">
      <path d="M0 296 H420 V310 H0 Z" fill="var(--tan)"/>
      <path d="M420 310 V230 Q420 205 445 205 H540 V310 Z" fill="var(--teal)"/>
    </svg>

    <div class="services">
      <h2 class="services__title">OUR SERVICES</h2>
      <div class="services__rule"></div>
      <ul class="services__list">
        <li class="services__item"><svg class="services__bolt" viewBox="0 0 11 15"><path d="M4 0h5L6 6h4L2 15l2-7H1z"/></svg>Residential &amp; Commercial</li>
        <li class="services__item"><svg class="services__bolt" viewBox="0 0 11 15"><path d="M4 0h5L6 6h4L2 15l2-7H1z"/></svg>Maintenance</li>
        <li class="services__item"><svg class="services__bolt" viewBox="0 0 11 15"><path d="M4 0h5L6 6h4L2 15l2-7H1z"/></svg>PV &amp; Battery servicing</li>
        <li class="services__item"><svg class="services__bolt" viewBox="0 0 11 15"><path d="M4 0h5L6 6h4L2 15l2-7H1z"/></svg>EV Chargers</li>
      </ul>
    </div>
  </section>

</body>
</html>
```